VELTRA Website Redesign in Wix

Task:
Create a new design for all pages of the VELTRA technology website in Wix. Specifications are:
Color palette preferences: black, white, gray, purple, blue. See VELTRA Ref Doc provided.
Please refer to the VELTRA_ref doc for a sample of the desired color palette
Typesetting must be in Montserrat
Brand will be that of a Marketing Technology company
Looking for vibrant, highly engaging images and organized, digestible flow. Open to suggestions
Required format is Wix.
VELTRA logo does NOT need to be redesigned. Please use the files provided for the VELTRA logo.
Look and feel
Each slider illustrates characteristics of the customer's brand and the style your logo design should communicate.

```html
<!DOCTYPE html>
<html lang="en">
<head>
<meta charset="utf-8">
<title>VELTRA – Self-service content delivery</title>
<link rel="stylesheet" href="https://fonts.googleapis.com/css2?family=Montserrat:wght@400;500;600;700&family=Lato:wght@400;700&display=swap">
<style>
:root{
  --navy:#17185a;
  --navy-deep:#0f1048;
  --purple:#4a1c8c;
  --purple-dark:#2a1370;
  --white:#ffffff;
  --ink:#1b1b2b;
  --gray-bg:#f1f1f3;
  --row-gray:#e9e9ec;
  --text-muted:#333344;
}
*{box-sizing:border-box;margin:0;padding:0}
html,body{width:1200px;height:3844px;overflow:hidden}
body{position:relative;font-family:'Montserrat',sans-serif;color:var(--ink);background:var(--white)}
.abs{position:absolute}

/* hero */
.hero{left:0;top:0;width:1200px;height:640px;background:linear-gradient(180deg,var(--navy-deep) 0%,var(--navy) 55%,#3a1f78 100%)}
.brand-box{left:131px;top:0;width:180px;height:57px;background:var(--purple);display:flex;align-items:center;justify-content:center;border-radius:0 0 6px 6px}
.brand-word{color:var(--white);font-weight:500;font-size:30px;letter-spacing:4px}
.nav{left:452px;top:0;width:620px;height:57px;background:var(--white);border-radius:0 0 6px 6px;display:flex;align-items:center;justify-content:center;gap:22px}
.nav a{font-size:12.5px;font-weight:500;color:var(--ink);text-decoration:none;letter-spacing:-.2px}
.hero-title{left:0;top:156px;width:1200px;text-align:center;color:var(--white);font-weight:600;font-size:35px;line-height:51px}
.btn-white{background:var(--white);color:var(--purple-dark);font-weight:600;font-size:16px;border-radius:5px;display:flex;align-items:center;justify-content:center}
.hero-btn{left:516px;top:337px;width:168px;height:56px}

.card{top:509px;width:226px;height:281px;border-radius:6px;overflow:hidden;display:flex;align-items:flex-end;justify-content:center;padding-bottom:38px;text-align:center;color:var(--white);font-weight:700;font-size:16px;line-height:25px;box-shadow:0 4px 10px rgba(0,0,0,.15)}
.card-1{left:131px;background:linear-gradient(135deg,#2b3140,#0f1420 60%,#3d4a56)}
.card-2{left:369px;background:linear-gradient(135deg,#6d7788,#2c3446 55%,#8a95a6)}
.card-3{left:604px;background:linear-gradient(135deg,#1a3d86,#3b8ed6 50%,#0d2a5c)}
.card-4{left:842px;background:linear-gradient(180deg,#3a2090,#5a1f8c);align-items:center;flex-direction:column;justify-content:flex-start;padding-top:66px;font-weight:600;font-size:16px}
.card-4 svg{margin-top:24px}

/* platform */
.section-title{font-weight:600;font-size:32px;text-align:center;color:var(--ink)}
.platform-title{left:0;top:890px;width:1200px}
.platform-copy{left:180px;top:944px;width:840px;text-align:center;font-family:'Lato',sans-serif;font-size:13px;line-height:25.5px;color:var(--text-muted)}
.compare-caption{left:0;top:1054px;width:1200px;text-align:center;font-size:12px;font-weight:600}
.compare{left:167px;top:1093px;width:858px;border-radius:8px;overflow:hidden;box-shadow:0 3px 10px rgba(0,0,0,.12);background:var(--white)}
.compare-head{height:65px;background:var(--navy);display:grid;grid-template-columns:136px repeat(6,120.3px);align-items:center;color:var(--white);font-weight:700}
.compare-head .feat{padding-left:27px;font-size:16px}
.compare-head .tech{display:flex;flex-direction:column;align-items:center;gap:2px;font-size:14px}
.compare-row{display:grid;grid-template-columns:136px repeat(6,120.3px);align-items:center;font-size:13px;font-weight:600}
.compare-row:nth-child(odd){background:var(--row-gray)}
.compare-row .label{text-align:center;line-height:21px;padding:0 22px}
.compare-row .mark{display:flex;justify-content:center}

/* awards */
.awards{left:0;top:1742px;width:1200px;height:773px;background:var(--gray-bg)}
.awards-title{left:0;top:1814px;width:1200px}
.award-visual{left:410px;top:1888px;width:380px;height:488px;border-radius:190px 190px 30px 30px;background:linear-gradient(160deg,#b9aaf0 0%,#f3c06a 35%,#ee9c86 65%,#e57fae 100%)}
.award{width:273px;height:224px;background:var(--white);border-radius:8px;box-shadow:0 3px 14px rgba(0,0,0,.10);padding:22px 14px 0 14px}
.award-top{display:flex;align-items:center;gap:22px;height:60px}
.badge{width:56px;height:56px;border-radius:4px;background:#d9d9de}
.award h3{font-size:17px;font-weight:600;line-height:25px}
.award p{font-size:11.6px;line-height:25px;margin-top:6px}
.stores{display:flex;gap:8px;margin-top:10px}
.store{height:31px;background:#0d0d10;color:var(--white);border-radius:4px;display:flex;align-items:center;gap:6px;padding:0 9px;font-size:12px;font-weight:500}
.store i{width:11px;height:11px;background:var(--white);border-radius:2px;display:block}
.award-l1{left:191px;top:1918px}
.award-l2{left:191px;top:2222px}
.award-r1{left:748px;top:1846px}
.award-r2{left:748px;top:2151px}

/* success */
.success{left:0;top:2515px;width:1200px;height:520px;background:linear-gradient(135deg,var(--navy) 0%,#1c1c6a 55%,#28247a 100%)}
.network{left:620px;top:2515px;width:580px;height:913px;background:radial-gradient(ellipse at 60% 40%,rgba(140,140,230,.35),rgba(40,30,120,0) 70%)}
.partners-band{left:0;top:3035px;width:1200px;height:393px;background:linear-gradient(180deg,var(--purple-dark),#3a1a86)}
.success-title{left:129px;top:2594px;color:var(--white);font-weight:600;font-size:32px}
.success-copy{left:130px;top:2647px;width:480px;color:var(--white);font-size:12px;font-weight:500;line-height:24px}
.success-btn{left:131px;top:2731px;width:167px;height:54px}

.contact{left:131px;top:2830px;width:469px;height:507px;background:var(--white);border-radius:8px;padding:30px 31px}
.contact h2{font-size:32px;font-weight:600}
.contact p{font-size:10.8px;font-weight:600;line-height:24px;margin-top:12px}
.field{position:absolute;border:1px solid #555;border-radius:4px;font-family:'Lato',sans-serif;font-size:11px;color:#333;padding:0 11px;display:flex;align-items:center}
.f-first{left:32px;top:180px;width:197px;height:50px}
.f-last{left:245px;top:180px;width:197px;height:50px}
.f-email{left:32px;top:247px;width:410px;height:50px}
.f-msg{left:32px;top:315px;width:410px;height:104px;align-items:flex-start;padding-top:14px}
.submit{position:absolute;left:32px;top:439px;width:410px;height:46px;border-radius:5px;background:linear-gradient(90deg,var(--navy),var(--purple));color:var(--white);font-weight:700;font-size:15px;display:flex;align-items:center;justify-content:center}

.partners-title{left:655px;top:3108px;color:var(--white);font-weight:600;font-size:27px;line-height:34px;text-transform:uppercase}
.partner{color:var(--white);font-weight:600}
.p1{left:655px;top:3194px;font-size:23px}
.p2{left:851px;top:3200px;font-size:15px}
.p3{left:688px;top:3270px;font-size:20px;line-height:26px;text-align:center;width:106px}
.p4{left:856px;top:3280px;font-size:12px;letter-spacing:1px}

/* footer */
.foot-brand{left:510px;top:3428px;width:180px;height:69px;background:var(--navy);display:flex;align-items:center;justify-content:center}
.foot-brand span{color:var(--white);font-size:32px;font-weight:500;letter-spacing:4px}
.rule{left:119px;width:961px;height:1px;background:#9a9aa2}
.rule-top{top:3528px}
.rule-bottom{top:3761px}
.foot-col{top:3566px}
.foot-col h4{font-size:15px;font-weight:600;margin-bottom:9px}
.foot-col li{list-style:none;font-family:'Lato',sans-serif;font-size:13px;line-height:24px;color:#333;display:flex;gap:10px}
.foot-col li b{font-weight:700;color:#333;width:10px;flex:none}
.col-contact{left:203px}
.col-contact li b{color:var(--navy)}
.col-nav{left:442px}
.col-social{left:658px}
.col-find{left:866px}
.foot-store{height:40px;width:130px;background:#0d0d10;color:var(--white);border-radius:6px;display:flex;align-items:center;gap:9px;padding:0 13px;font-size:15px;font-weight:500;margin-bottom:12px;border:1px solid #888}
.foot-store i{width:16px;height:16px;background:var(--white);border-radius:3px;display:block}
.copyright{left:0;top:3782px;width:1200px;text-align:center;font-size:13px;color:#333}
</style>
</head>
<body>
<svg width="0" height="0" style="position:absolute">
  <defs>
    <symbol id="yes" viewBox="0 0 40 40"><circle cx="20" cy="20" r="20" fill="#2aa45a"/><path d="M11 20.5l6 6 12-13" fill="none" stroke="#fff" stroke-width="4.5" stroke-linecap="round" stroke-linejoin="round"/></symbol>
    <symbol id="no" viewBox="0 0 40 40"><circle cx="20" cy="20" r="20" fill="#e63a3a"/><path d="M13 13l14 14M27 13L13 27" stroke="#fff" stroke-width="4.5" stroke-linecap="round"/></symbol>
  </defs>
</svg>

<header>
  <div class="abs hero"></div>
  <div class="abs brand-box"><span class="brand-word">VELTRA</span></div>
  <nav class="abs nav">
    <a href="#">HOME</a><a href="#">HOW IT WORKS</a><a href="#">VELTRA APPLICATIONS</a><a href="#">COMPANY</a><a href="#">CONTACT US</a>
  </nav>
  <h1 class="abs hero-title">Increase and perfect your connection<br>with consumers using VELTRA™’s patented<br>self-service content delivery technology</h1>
  <div class="abs btn-white hero-btn">Learn More</div>

  <div class="abs card card-1" role="img" aria-label="Photo of a hand touching a glowing subscription service interface">Corporate<br>Subscriptions</div>
  <div class="abs card card-2" role="img" aria-label="Photo of a person typing on a laptop with chart overlay">AD tech<br>licensing</div>
  <div class="abs card card-3" role="img" aria-label="Photo of a hand holding a glowing cloud integration graphic">Platform<br>Integrations</div>
  <div class="abs card card-4">Explore Our<br>Saas Platform
    <svg width="44" height="80" viewBox="0 0 44 80"><path d="M22 2v74M4 58l18 18 18-18" fill="none" stroke="#fff" stroke-width="2.5"/></svg>
  </div>
</header>

<section>
  <h2 class="abs section-title platform-title">Our Revolutionary Platform</h2>
  <p class="abs platform-copy">Whether you’re marketing software, selling a product, or looking to close a deal – find out your target market and quickly modify your campaigns to reach consumers silently and securely. Our platform goes far beyond basic ad optimization to deliver individualized content that immediately increases engagement over any communication medium with embedded tones.</p>
  <p class="abs compare-caption">Current Technology vs VELTRA™</p>

  <div class="abs compare">
    <div class="compare-head">
      <div class="feat">Features</div>
      <div class="tech"><svg width="34" height="26" viewBox="0 0 34 26"><g stroke="#fff" stroke-width="2.4" stroke-linecap="round"><path d="M3 10v6M9 6v14M15 2v22M21 6v14M27 9v8M32 11v4"/></g></svg>VELTRA</div>
      <div class="tech"><svg width="34" height="26" viewBox="0 0 34 26" fill="none" stroke="#fff" stroke-width="2.4" stroke-linecap="round"><path d="M3 9a20 20 0 0 1 28 0M8 14a13 13 0 0 1 18 0M12.5 19a6 6 0 0 1 9 0"/><circle cx="17" cy="23" r="1.5" fill="#fff"/></svg>Wifi</div>
      <div class="tech"><svg width="34" height="26" viewBox="0 0 34 26"><circle cx="17" cy="13" r="9" fill="none" stroke="#fff" stroke-width="2.4"/><circle cx="17" cy="13" r="3" fill="#fff"/></svg>Radio Link</div>
      <div class="tech"><svg width="40" height="26" viewBox="0 0 40 26" fill="none" stroke="#fff" stroke-width="2" stroke-linecap="round"><circle cx="20" cy="12" r="3" fill="#fff"/><path d="M14 6a9 9 0 0 0 0 12M26 6a9 9 0 0 1 0 12M10 3a14 14 0 0 0 0 18M30 3a14 14 0 0 1 0 18"/></svg>RFID</div>
      <div class="tech"><svg width="34" height="26" viewBox="0 0 34 26" fill="none" stroke="#fff" stroke-width="2.2" stroke-linecap="round"><path d="M8 8l6 6-6 6M18 5a11 11 0 0 1 0 16M23 2a16 16 0 0 1 0 22"/></svg>NFC</div>
      <div class="tech"><svg width="34" height="26" viewBox="0 0 34 26" fill="none" stroke="#fff" stroke-width="2"><circle cx="10" cy="15" r="4"/><circle cx="25" cy="7" r="4"/><circle cx="25" cy="21" r="3"/><path d="M13.5 13l8-4M13.5 17l8.5 3"/></svg>Social</div>
    </div>

    <div>
      <div class="compare-row" style="height:80px"><div class="label">Operates without a network</div>
        <div class="mark"><svg width="40" height="40"><use href="#yes"/></svg></div><div class="mark"><svg width="40" height="40"><use href="#no"/></svg></div><div class="mark"><svg width="40" height="40"><use href="#no"/></svg></div><div class="mark"><svg width="40" height="40"><use href="#no"/></svg></div><div class="mark"><svg width="40" height="40"><use href="#no"/></svg></div><div class="mark"><svg width="40" height="40"><use href="#no"/></svg></div></div>
      <div class="compare-row" style="height:88px"><div class="label">Operates without live power</div>
        <div class="mark"><svg width="40" height="40"><use href="#yes"/></svg></div><div class="mark"><svg width="40" height="40"><use href="#no"/></svg></div><div class="mark"><svg width="40" height="40"><use href="#no"/></svg></div><div class="mark"><svg width="40" height="40"><use href="#no"/></svg></div><div class="mark"><svg width="40" height="40"><use href="#no"/></svg></div><div class="mark"><svg width="40" height="40"><use href="#no"/></svg></div></div>
      <div class="compare-row" style="height:80px"><div class="label">transmits data securely</div>
        <div class="mark"><svg width="40" height="40"><use href="#yes"/></svg></div><div class="mark"><svg width="40" height="40"><use href="#yes"/></svg></div><div class="mark"><svg width="40" height="40"><use href="#yes"/></svg></div><div class="mark"><svg width="40" height="40"><use href="#yes"/></svg></div><div class="mark"><svg width="40" height="40"><use href="#yes"/></svg></div><div class="mark"><svg width="40" height="40"><use href="#no"/></svg></div></div>
      <div class="compare-row" style="height:88px"><div class="label">Private</div>
        <div class="mark"><svg width="40" height="40"><use href="#yes"/></svg></div><div class="mark"><svg width="40" height="40"><use href="#yes"/></svg></div><div class="mark"><svg width="40" height="40"><use href="#yes"/></svg></div><div class="mark"><svg width="40" height="40"><use href="#yes"/></svg></div><div class="mark"><svg width="40" height="40"><use href="#yes"/></svg></div><div class="mark"><svg width="40" height="40"><use href="#no"/></svg></div></div>
      <div class="compare-row" style="height:80px"><div class="label">customization</div>
        <div class="mark"><svg width="40" height="40"><use href="#yes"/></svg></div><div class="mark"><svg width="40" height="40"><use href="#yes"/></svg></div><div class="mark"><svg width="40" height="40"><use href="#yes"/></svg></div><div class="mark"><svg width="40" height="40"><use href="#yes"/></svg></div><div class="mark"><svg width="40" height="40"><use href="#yes"/></svg></div><div class="mark"><svg width="40" height="40"><use href="#yes"/></svg></div></div>
      <div class="compare-row" style="height:82px"><div class="label">caried by audio soundwaves</div>
        <div class="mark"><svg width="40" height="40"><use href="#yes"/></svg></div><div class="mark"><svg width="40" height="40"><use href="#no"/></svg></div><div class="mark"><svg width="40" height="40"><use href="#no"/></svg></div><div class="mark"><svg width="40" height="40"><use href="#no"/></svg></div><div class="mark"><svg width="40" height="40"><use href="#no"/></svg></div><div class="mark"><svg width="40" height="40"><use href="#no"/></svg></div></div>
    </div>
  </div>
</section>

<section>
  <div class="abs awards"></div>
  <h2 class="abs section-title awards-title">Our Awards</h2>
  <div class="abs award-visual" role="img" aria-label="Illustration of a smartphone showing the app splash screen over soft coloured shapes"></div>

  <div class="abs award award-l1">
    <div class="award-top"><div class="badge"></div><h3>Lorem ipsum<br>dolor</h3></div>
    <p>Lorem ipsum dolor sit amet, consectetur adipiscing elit, sed do eiusmod tempor incididunt ut labore et dolore.</p>
    <div class="stores"><div class="store"><i></i>AppHub</div><div class="store"><i></i>PlayMart</div></div>
  </div>
  <div class="abs award award-l2">
    <div class="award-top"><div class="badge"></div><h3>Lorem ipsum<br>dolor</h3></div>
    <p>Lorem ipsum dolor sit amet, consectetur adipiscing elit, sed do eiusmod tempor incididunt ut labore et dolore.</p>
    <div class="stores"><div class="store"><i></i>AppHub</div><div class="store"><i></i>PlayMart</div></div>
  </div>
  <div class="abs award award-r1">
    <div class="award-top"><div class="badge"></div><h3>Lorem ipsum<br>dolor</h3></div>
    <p>Lorem ipsum dolor sit amet, consectetur adipiscing elit, sed do eiusmod tempor incididunt ut labore et dolore.</p>
    <div class="stores"><div class="store"><i></i>AppHub</div><div class="store"><i></i>PlayMart</div></div>
  </div>
  <div class="abs award award-r2">
    <div class="award-top"><div class="badge"></div><h3>Lorem ipsum<br>dolor</h3></div>
    <p>Lorem ipsum dolor sit amet, consectetur adipiscing elit, sed do eiusmod tempor incididunt ut labore et dolore.</p>
    <div class="stores"><div class="store"><i></i>AppHub</div><div class="store"><i></i>PlayMart</div></div>
  </div>
</section>

<section>
  <div class="abs success"></div>
  <div class="abs partners-band"></div>
  <div class="abs network" role="img" aria-label="Abstract glowing network of connected points"></div>

  <h2 class="abs success-title">Proven Success in Innovation</h2>
  <p class="abs success-copy">Lorem ipsum dolor sit amet, consectetur adipiscing elit, sed do eiusmod tempor incididunt ut labore et dolore magna aliqua. Ut enim ad minim veniam, quis nostrud exercitation ullamco laboris nisi ut aliquip.</p>
  <div class="abs btn-white success-btn">Learn More</div>

  <form class="abs contact">
    <h2>Get in Touch</h2>
    <p>Lorem ipsum dolor sit amet, consectetur adipiscing elit, sed do eiusmod tempor incididunt ut labore et dolore magna aliqua. Ut enim ad minim veniam, quis nostrud exercitation ullamco laboris nisi ut aliquip.</p>
    <div class="field f-first">First Name</div>
    <div class="field f-last">Last Name</div>
    <div class="field f-email">Email Address</div>
    <div class="field f-msg">Leave us a message..</div>
    <div class="submit">SUBMIT</div>
  </form>

  <h2 class="abs partners-title">Our customers and<br>partners</h2>
  <div class="abs partner p1">Cloudkeep</div>
  <div class="abs partner p2">GREYFIELD LTD</div>
  <div class="abs partner p3">Harbor Art Fair</div>
  <div class="abs partner p4">CORVALIS &amp; REED</div>
</section>

<footer>
  <div class="abs foot-brand"><span>VELTRA</span></div>
  <div class="abs rule rule-top"></div>
  <div class="abs foot-col col-contact"><h4>CONTACT</h4>
    <ul><li><b>✉</b>info@veltratech.example</li><li><b>✆</b>1-866-555-0148</li><li><b>⌖</b>Lorem ipsum dolor sit amet<br>consectetur adipiscing.</li></ul></div>
  <div class="abs foot-col col-nav"><h4>NAVIGATION</h4>
    <ul><li><b>»</b>Home</li><li><b>»</b>How it works</li><li><b>»</b>VELTRA Applications</li><li><b>»</b>Company</li><li><b>»</b>Contact Us</li></ul></div>
  <div class="abs foot-col col-social"><h4>SOCIAL MEDIA</h4>
    <ul><li><b>»</b>Chatroom</li><li><b>»</b>Livecast</li><li><b>»</b>Socialnet</li><li><b>»</b>Clipstream</li><li><b>»</b>Chirper</li><li><b>»</b>Worklink</li></ul></div>
  <div class="abs foot-col col-find"><h4>FIND US ON</h4>
    <div class="foot-store"><i></i>PlayMart</div>
    <div class="foot-store"><i></i>AppHub</div>
  </div>
  <div class="abs rule rule-bottom"></div>
  <p class="abs copyright">© copyrights 2022 VELTRA &nbsp;|&nbsp; All Rights Reserved</p>
</footer>
</body>
</html>
```